Brisk Tailor Signage

This design is for "signage" that we intend to get produced.
A couple of different designs that say "Brisk Tailor on Guard" and "Beware of Brisk Tailor"
It should also have our logo (BT) plus our logo with the hand and dog paw. We would also like the main picture of the sign to be the attached. We would like a classy sophisticated look similar to our logo you designed.
Our designs will go on consumers gates/entrances to warn people there is a dog on the premises. I will get a better quality picture of the dog.

```html
<!DOCTYPE html>
<html lang="en">
<head>
<meta charset="utf-8">
<title>Brisk Tailor Signage</title>
<link rel="stylesheet" href="https://fonts.googleapis.com/css2?family=Passion+One:wght@700&family=Poppins:wght@600&display=swap">
<style>
  :root {
    --stage: #d4d5d8;
    --sign-white: #ffffff;
    --periwinkle: #9aaad6;
    --ink: #3b3b3b;
    --dog-dark: #3e3e3e;
    --dog-light: #4a4a4a;
    --bolt-light: #f4f4f4;
    --bolt-dark: #b9b9b9;
  }
  * { margin: 0; padding: 0; box-sizing: border-box; }
  html, body { width: 1200px; height: 765px; overflow: hidden; background: var(--stage); }
  .canvas { position: relative; width: 1200px; height: 765px; background: var(--stage); }

  .sign {
    position: absolute; top: 51px; width: 470px; height: 665px;
    background: var(--sign-white); overflow: hidden;
  }
  .sign--guard { left: 90px; }
  .sign--beware { left: 644px; }

  .sign__band { position: absolute; inset: 0; width: 470px; height: 665px; }

  .bolt {
    position: absolute; width: 21px; height: 21px; border-radius: 50%;
    background: linear-gradient(90deg, var(--bolt-light) 30%, var(--bolt-dark));
  }
  .bolt--tl { left: 60px; top: 30px; }
  .bolt--tr { left: 390px; top: 30px; }
  .bolt--bl { left: 60px; top: 620px; }
  .bolt--br { left: 390px; top: 620px; }

  .headline { position: absolute; color: var(--ink); line-height: 1; white-space: nowrap; }
  .headline__name { font-family: "Poppins", sans-serif; font-weight: 600; font-size: 52px; letter-spacing: 0.5px; }
  .headline__call { font-family: "Passion One", sans-serif; font-weight: 700; text-transform: uppercase; }

  .sign--guard .headline__name { position: absolute; left: 88px; top: 58px; }
  .sign--guard .headline__call { position: absolute; left: 86px; top: 118px; font-size: 82px; letter-spacing: 2px; }

  .sign--beware .headline__call { position: absolute; left: 80px; top: 58px; font-size: 72px; letter-spacing: 2px; }
  .sign--beware .headline__name { position: absolute; left: 82px; top: 122px; }

  .dog-photo {
    position: absolute; left: 21px; top: 208px; width: 322px; height: 446px;
    background: linear-gradient(160deg, var(--dog-light), var(--dog-dark));
    border-radius: 60px 40px 8px 30px;
  }

  .marks { position: absolute; left: 331px; top: 538px; width: 115px; height: 72px; }
  .marks__badge {
    position: absolute; top: 11px; width: 48px; height: 48px; border-radius: 50%;
    border: 1.5px solid var(--periwinkle);
    display: flex; align-items: center; justify-content: center;
    font-family: "Poppins", sans-serif; font-weight: 600; font-size: 15px; color: var(--periwinkle);
  }
  .marks__badge--care { left: 0; border-width: 2px; }
  .marks__badge--monogram { left: 61px; }
  .marks__divider { position: absolute; left: 54px; top: 0; width: 1.5px; height: 72px; background: var(--ink); }
</style>
</head>
<body>
<main class="canvas">

  <section class="sign sign--guard">
    <svg class="sign__band" viewBox="0 0 470 665" aria-hidden="true"><polygon points="0,0 470,0 0,665" fill="var(--periwinkle)"/></svg>
    <span class="bolt bolt--tl"></span><span class="bolt bolt--tr"></span>
    <span class="bolt bolt--bl"></span><span class="bolt bolt--br"></span>
    <h1 class="headline">
      <span class="headline__name">Brisk Tailor</span>
      <span class="headline__call">On Guard</span>
    </h1>
    <div class="dog-photo" role="img" aria-label="Photo of the client's dark seated dog, shown in low-poly style"></div>
    <div class="marks">
      <span class="marks__badge marks__badge--care"></span>
      <span class="marks__divider"></span>
      <span class="marks__badge marks__badge--monogram">BT</span>
    </div>
  </section>

  <section class="sign sign--beware">
    <svg class="sign__band" viewBox="0 0 470 665" aria-hidden="true"><polygon points="0,0 470,0 0,665" fill="var(--periwinkle)"/></svg>
    <span class="bolt bolt--tl"></span><span class="bolt bolt--tr"></span>
    <span class="bolt bolt--bl"></span><span class="bolt bolt--br"></span>
    <h1 class="headline">
      <span class="headline__call">Beware of</span>
      <span class="headline__name">Brisk Tailor</span>
    </h1>
    <div class="dog-photo" role="img" aria-label="Photo of the client's dark seated dog, shown in low-poly style"></div>
    <div class="marks">
      <span class="marks__badge marks__badge--care"></span>
      <span class="marks__divider"></span>
      <span class="marks__badge marks__badge--monogram">BT</span>
    </div>
  </section>

</main>
</body>
</html>
```